Business card for builder specialising in renovations.

Need a card for our building business. Business name is under Marcus Pellow.
Have licence number on card ( 527196K)
Contact number (0400 583 214)
Want to work on logo for some business cards and shirts - something with MP or MPB or open to ideas??
No animations, No hammers. Something sharp and eye catching.
Highlight that we are a renovation specialist. Simple on front with extra details on back with some lines to jot down things.

Target Market(s)

Renovators

Industry/Entity Type

Building

Contact Information for Business Card

2 sided with room on back to jot things down.
Extra details on back so front can be simple ..like, renovations, bathrooms, decks, extensions, new builds,

Logo Text

MP

Font styles to use
Serif

Requirements
Must have
• Eye catching design .
• Name : Marcus pellow
• Licence number
• Contact number - 0400583214
Nice to have
• Some logo design that we can carry through to other forms of advertising
• Local builder
• Quality work
Should not have
• No animations

```html
<!DOCTYPE html>
<html lang="en">
<head>
<meta charset="utf-8">
<title>Marcus Pellow – Business Card</title>
<link href="https://fonts.googleapis.com/css2?family=Josefin+Sans:wght@400;600;700&display=swap" rel="stylesheet">
<style>
  :root {
    --backdrop: #e6e8e9;
    --card: #ffffff;
    --ink: #1d1d1f;
    --accent-red: #e41e26;
    --bar-black: #1a1a1a;
    --card-shadow: rgba(0, 0, 0, 0.12);
  }
  * { margin: 0; padding: 0; box-sizing: border-box; }
  html, body {
    width: 1200px;
    height: 900px;
    overflow: hidden;
    background: var(--backdrop);
    font-family: "Josefin Sans", sans-serif;
    color: var(--ink);
  }
  .canvas {
    position: relative;
    width: 1200px;
    height: 900px;
  }
  .card {
    position: absolute;
    top: 291px;
    width: 520px;
    height: 318px;
    background: var(--card);
    box-shadow: 0 2px 3px var(--card-shadow), 0 12px 30px var(--card-shadow);
  }
  .card--front { left: 620px; }
  .card--back { left: 60px; }

  /* Front */
  .brand-mark {
    position: absolute;
    left: 50%;
    top: 62px;
    transform: translateX(-50%);
    display: flex;
    align-items: center;
    gap: 12px;
  }
  .brand-mark__square {
    width: 22px;
    height: 22px;
    background: var(--accent-red);
  }
  .brand-mark__initials {
    font-size: 62px;
    font-weight: 700;
    letter-spacing: 2px;
    line-height: 1;
    color: var(--ink);
  }
  .owner-name {
    position: absolute;
    left: 0;
    right: 0;
    top: 158px;
    text-align: center;
    font-size: 22px;
    font-weight: 700;
    letter-spacing: 1px;
  }
  .contact-line {
    position: absolute;
    right: 34px;
    top: 200px;
    font-size: 15px;
    font-weight: 600;
    letter-spacing: 0.5px;
  }
  .licence-line {
    position: absolute;
    left: 34px;
    bottom: 30px;
    font-size: 15px;
    font-weight: 600;
    letter-spacing: 0.5px;
  }

  /* Back */
  .bar {
    position: absolute;
    width: 8px;
  }
  .bar--black {
    left: 38px;
    top: 22px;
    height: 92px;
    background: var(--bar-black);
  }
  .bar--red {
    left: 104px;
    top: 100px;
    height: 196px;
    background: var(--accent-red);
  }
  .back-mark {
    position: absolute;
    left: 70px;
    top: 30px;
    display: flex;
    align-items: center;
    gap: 6px;
  }
  .back-mark__square {
    width: 9px;
    height: 9px;
    background: var(--accent-red);
  }
  .back-mark__initials {
    font-size: 24px;
    font-weight: 700;
    line-height: 1;
  }
  .tagline {
    position: absolute;
    left: 76px;
    top: 296px;
    transform-origin: 0 0;
    transform: rotate(-90deg);
    font-size: 15px;
    font-weight: 600;
    letter-spacing: 1px;
    white-space: nowrap;
  }
  .services {
    position: absolute;
    left: 126px;
    top: 112px;
    list-style: none;
    font-size: 21px;
    line-height: 34px;
  }
</style>
</head>
<body>
<main class="canvas">
  <section class="card card--back" aria-label="Card back">
    <span class="bar bar--black"></span>
    <div class="back-mark">
      <span class="back-mark__square"></span>
      <span class="back-mark__initials">MP</span>
    </div>
    <span class="bar bar--red"></span>
    <p class="tagline">Renovate with us......</p>
    <ul class="services">
      <li>Renovations</li>
      <li>Bathrooms</li>
      <li>Decks</li>
      <li>Extensions</li>
      <li>New Builds etc</li>
    </ul>
  </section>

  <section class="card card--front" aria-label="Card front">
    <div class="brand-mark">
      <span class="brand-mark__square"></span>
      <span class="brand-mark__initials">MP</span>
    </div>
    <h1 class="owner-name">Marcus Pellow</h1>
    <p class="contact-line">Contact : 0400 583 214</p>
    <p class="licence-line">Licence Number : 527196k</p>
  </section>
</main>
</body>
</html>
```